Modern Innovative Business Card Design

We require a nice, modern, clean business card design, ready for upload to Cardwello. Our company develops online banking software solutions for small financial insitutions. The design should be clean, professional, but yet not "corporate boring". See www.fintrola.com for an idea of business image and profile. The design should communicate innovation, be modern and fresh, yet look professional and established.

Target Market(s)

Finance industry, bankers, entrepreneurs

Industry/Entity Type

Financial

Contact Information for Business Card

Daniel Hargreave
CEO

FINTROLA BV
Lindenhofstraat 38
1072 KD Amsterdam
The Netherlands

Phone: +31 20 517 8063
Direct: +31 20 446 1975
Skype: daniel.fintrola
ceo@fintrola.com
www.fintrola.com

Font styles to use
Sans Serif

Requirements
Must have
• Should look clean, modern and professional. File should be ready for upload to cardwello.
Should not have
• Boring standard corporate layout

```html
<!DOCTYPE html>
<html lang="en">
<head>
<meta charset="utf-8">
<title>Fintrola Business Card</title>
<link href="https://fonts.googleapis.com/css2?family=Open+Sans:wght@400;600;700&family=Questrial&display=swap" rel="stylesheet">
<style>
  :root {
    --stage: #ecebe8;
    --card-white: #ffffff;
    --charcoal: #58595b;
    --text-gray: #5f6062;
    --lime: #8cc63f;
    --soft-white: #e9e9e9;
  }
  * { margin: 0; padding: 0; box-sizing: border-box; }
  html, body { width: 1200px; height: 900px; overflow: hidden; }
  body {
    background: var(--stage);
    font-family: "Open Sans", Arial, sans-serif;
    position: relative;
  }
  .card {
    position: absolute;
    left: 300px;
    width: 600px;
    height: 343px;
    box-shadow: 0 6px 18px rgba(0,0,0,0.18);
    overflow: hidden;
  }
  .card-back { top: 60px; background: var(--charcoal); }
  .card-front { top: 470px; background: var(--card-white); }

  .back-brand {
    position: absolute;
    right: 48px;
    bottom: 78px;
    font-family: "Questrial", Arial, sans-serif;
    font-size: 46px;
    letter-spacing: 3px;
    color: var(--card-white);
  }
  .back-web {
    position: absolute;
    right: 50px;
    bottom: 48px;
    font-size: 15px;
    letter-spacing: 5.5px;
    color: var(--soft-white);
  }

  .front-brand {
    position: absolute;
    right: 36px;
    top: 46px;
    font-family: "Questrial", Arial, sans-serif;
    font-size: 58px;
    letter-spacing: 3px;
    color: var(--text-gray);
  }
  .person { position: absolute; left: 32px; top: 34px; }
  .person-name { font-size: 22px; font-weight: 700; color: var(--lime); line-height: 1.1; }
  .person-role { font-size: 13px; color: var(--text-gray); margin-top: 3px; }
  .contact-list { list-style: none; position: absolute; left: 32px; top: 100px; }
  .contact-list li {
    display: flex; align-items: center; gap: 8px;
    font-size: 13px; color: var(--text-gray); line-height: 21px;
  }
  .contact-icon { width: 13px; height: 13px; flex: none; }
  .address {
    position: absolute;
    right: 40px;
    top: 218px;
    text-align: right;
    font-size: 14px;
    line-height: 17px;
    color: var(--text-gray);
  }
  .front-graphics { position: absolute; inset: 0; }
  .front-web {
    position: absolute;
    left: 352px;
    bottom: 12px;
    font-size: 16px;
    letter-spacing: 4.5px;
    color: var(--soft-white);
  }
</style>
</head>
<body>

  <section class="card card-back" aria-label="Card back">
    <div class="back-brand">FINTROLA</div>
    <div class="back-web">www.fintrola.com</div>
  </section>

  <section class="card card-front" aria-label="Card front">
    <svg class="front-graphics" width="600" height="343" viewBox="0 0 600 343">
      <line x1="150" y1="200" x2="572" y2="200" stroke="var(--lime)" stroke-width="1.2"/>
      <polygon points="0,298 312,298 300,312 0,312" fill="var(--lime)"/>
      <polygon points="0,316 298,316 322,292 600,292 600,343 0,343" fill="var(--charcoal)"/>
    </svg>

    <div class="front-brand">FINTROLA</div>

    <div class="person">
      <div class="person-name">Daniel Hargreave</div>
      <div class="person-role">CEO</div>
    </div>

    <ul class="contact-list">
      <li>
        <svg class="contact-icon" viewBox="0 0 16 16"><path fill="var(--lime)" d="M3.5 1.5l2.5 0 1 3.5-1.6 1.2c.8 1.8 2.2 3.2 4 4l1.2-1.6 3.5 1v2.5c0 .8-.7 1.4-1.5 1.4C6.8 13.5 2.5 9.2 2.1 3c0-.8.6-1.5 1.4-1.5z"/></svg>
        +31 20 517 8063
      </li>
      <li>
        <svg class="contact-icon" viewBox="0 0 16 16"><path fill="var(--lime)" d="M3.5 1.5l2.5 0 1 3.5-1.6 1.2c.8 1.8 2.2 3.2 4 4l1.2-1.6 3.5 1v2.5c0 .8-.7 1.4-1.5 1.4C6.8 13.5 2.5 9.2 2.1 3c0-.8.6-1.5 1.4-1.5z"/></svg>
        +31 20 446 1975
      </li>
      <li>
        <svg class="contact-icon" viewBox="0 0 16 16"><circle cx="8" cy="8" r="7" fill="var(--lime)"/></svg>
        daniel.fintrola
      </li>
      <li>
        <svg class="contact-icon" viewBox="0 0 16 16"><rect x="1" y="3" width="14" height="10" rx="1" fill="var(--lime)"/><path d="M1.5 3.8L8 9l6.5-5.2" stroke="#fff" stroke-width="1.2" fill="none"/></svg>
        ceo@fintrola.com
      </li>
    </ul>

    <address class="address" style="font-style:normal">
      FINTROLA BV, Lindenhofstraat 38<br>
      1072 KD Amsterdam<br>
      The Netherlands
    </address>

    <div class="front-web">www.fintrola.com</div>
  </section>

</body>
</html>
```